Eco-friendly printer cartridges and toners packaging

Dear designers,

we are looking for a new packaging design for remanufactured printer consumables products. The design should clearly communicate ecology and economy (check inspirations attached - we like them :) ). To understand the ecological impact you can watch the presentation at http://www.verdaplix.sk/ecology.html . You can find also more information about the brand at http://www.verdaplix.sk/index1.html .

We currently need universal design for following sizes of product:

cartridges:

1. 60x25x90 mm
2. 60x45x90 mm
3. 80x45x120 mm

laser toners:

4. 178x110x345 mm

They all should be recoginezed at the first sight, that it is the same brand and by buying this product the customer contributes to saving enviroment and supports socially responsible company, while it also saves his/hers money.

The final packaging will be in blister.

And be as creative as possible. Its all up to you.

Feel free to ask as many questions as needed.

You do not have to stick to the packaging design and sizes in the attachement. The only thing you need to stick to is the actual product measures.

Reason: As we have a little more time than we expected, we postpone the deadline. We also have a lot of accepted project invitations and we are expecting the delivery. Thank you for understanding. Radim

Target Market(s)

Anyone who buys printer consumables. It should attract everyone who thinks ecologically and wants to save some money

Industry/Entity Type

It Company

Requirements
Must have
• 1. logo - will be attached (if you dont like current logo you can try to design new one)
2. ecological messages - up to you
3. Slovak and English manual - will be attached
4. Pictograms - will be attached (can be redisigned)
5. Compatibility - which printers is the cartridge/toner compatible with (blank space to be filled in)
6. Slovak and English copyright disclaimer - will be attached
7. Colour identification (black, cyan, magenta....)
8. ISO 9001 / ISO 14001
9. Made in Europe
10. Production Date
11. Part no.
12. Use before text - will be attached
Nice to have
• 1.we are currently remanufacturing cartridges and toners for printers of 12 different brands (dovrent, zq, bivot, murly...) The packaging should be somehow differentiated for each different brand (either by colour / it can be different colour of some line, or the whole backgroud or just some spot on the packaging/, different fruit on the packaging, or whatever you consider to be the best option.

2. nature in the design

```html
<!DOCTYPE html>
<html lang="en">
<head>
<meta charset="utf-8">
<title>Eco Ink Cartridge – Box Dieline</title>
<link href="https://fonts.googleapis.com/css2?family=Montserrat:wght@800;900&family=Source+Sans+3:wght@400;600;700&display=swap" rel="stylesheet">
<style>
  :root{
    --kraft:#b89a74;
    --paper:#ffffff;
    --ink:#111111;
    --sky:#00aeef;
    --lime:#b5cf3a;
    --fold:#ffffff;
  }
  html,body{margin:0;padding:0;overflow:hidden;background:var(--paper);}
  .canvas{position:relative;width:1200px;height:1163px;overflow:hidden;background:var(--paper);
    font-family:"Source Sans 3",Arial,sans-serif;color:var(--ink);}
  .dieline{position:absolute;left:0;top:0;}
  .layer{position:absolute;}
  .manual{left:114px;top:526px;width:290px;font-size:11.3px;line-height:14.2px;}
  .manual p{margin:0;}
  .manual .gap{height:14px;}
  .manual .lang{color:var(--paper);font-weight:700;}
  .manual strong{font-weight:700;}
  .manual .just{text-align:justify;}
  .manual hr{border:0;border-top:1px solid var(--paper);margin:5px 0 6px;}
  .brand{left:793px;top:529px;font-size:31px;font-weight:400;letter-spacing:-0.3px;color:var(--ink);display:flex;align-items:center;gap:5px;}
  .brand .dot{width:16px;height:16px;border-radius:50%;background:var(--lime);}
  .title{font-family:"Montserrat",Arial,sans-serif;font-weight:900;line-height:0.98;}
  .title .eco{color:var(--lime);}
  .title-front{left:695px;top:752px;font-size:50px;text-align:right;width:238px;}
  .title-front .line2{font-size:41px;letter-spacing:0.5px;}
  .title-side{left:953px;top:537px;font-size:41px;}
  .title-side .line2{font-size:33px;letter-spacing:0.4px;}
  .compat-label{left:790px;top:848px;width:141px;text-align:right;color:var(--paper);font-size:12px;}
  .compat-box{left:695px;top:864px;width:236px;height:74px;border:1px solid var(--paper);border-radius:4px;box-sizing:border-box;}
  .prod-label{left:697px;top:961px;font-size:11px;}
  .prod-box{left:697px;top:981px;width:154px;height:24px;}
  .prod-box::before,.prod-box::after{content:"";position:absolute;top:0;width:5px;height:24px;border:1px solid var(--ink);box-sizing:border-box;}
  .prod-box::before{left:0;border-right:0;} .prod-box::after{right:0;border-left:0;}
  .specs{left:952px;top:880px;font-size:12.5px;line-height:20.5px;}
  .specs p{margin:0;}
</style>
</head>
<body>
<div class="canvas">
  <svg class="dieline" width="1200" height="1163" viewBox="0 0 1200 1163" xmlns="http://www.w3.org/2000/svg">
    <defs>
      <linearGradient id="foliage" x1="0" y1="0" x2="1" y2="1">
        <stop offset="0" stop-color="#b5cf3a" stop-opacity="0.55"/>
        <stop offset="1" stop-color="#b5cf3a" stop-opacity="0.35"/>
      </linearGradient>
    </defs>
    <g fill="var(--kraft)">
      <path d="M108 40 H398 L408 62 V517 H108 Z"/>
      <path d="M103 517 L48 533 V928 L103 945 Z"/>
      <rect x="103" y="517" width="1047" height="428"/>
      <path d="M418 517 V492 L458 375 H612 L628 420 V517 Z"/>
      <path d="M942 517 V375 H1110 L1150 492 V517 Z"/>
      <rect x="630" y="300" width="310" height="217"/>
      <path d="M630 300 V270 Q630 232 672 232 H898 Q940 232 940 270 V300 Z"/>
      <path d="M103 945 H413 L370 990 L355 1050 H305 V1115 H103 Z"/>
      <path d="M413 945 H630 V1050 H455 L418 990 Z"/>
      <path d="M630 945 H940 L900 990 L880 1050 H835 V1115 H630 Z"/>
      <path d="M940 945 H1150 L1110 1010 L1060 1050 H970 L945 990 Z"/>
    </g>
    <path role="img" aria-label="Blue wave illustration with leaping dolphins" fill="var(--sky)"
      d="M108 40 H398 L408 62 V90 C330 110 190 120 165 190 C150 240 190 280 108 300 Z M108 300 C200 330 140 380 180 420 C230 470 330 480 408 500 V517 H108 Z"/>
    <g fill="var(--paper)">
      <rect x="175" y="210" width="165" height="32" rx="16"/><circle cx="258" cy="226" r="30"/>
      <rect x="175" y="355" width="165" height="32" rx="16"/><circle cx="258" cy="370" r="30"/>
    </g>
    <rect role="img" aria-label="Stylised tree with green striped leaves and blue ink-drop fruits" x="425" y="525" width="435" height="415" rx="120" fill="url(#foliage)"/>
    <g fill="none" stroke="var(--paper)" stroke-width="1.6">
      <rect x="952" y="805" width="22" height="22" rx="2"/><rect x="992" y="805" width="22" height="22" rx="2"/>
      <rect x="1032" y="805" width="22" height="22" rx="2"/><rect x="1072" y="805" width="22" height="22" rx="2"/>
      <rect x="1112" y="805" width="22" height="22" rx="2"/>
      <rect x="952" y="846" width="22" height="22" rx="2"/><rect x="992" y="846" width="22" height="22" rx="2"/>
      <rect x="1032" y="846" width="22" height="22" rx="2"/><rect x="1072" y="846" width="22" height="22" rx="2"/>
    </g>
    <g stroke="var(--fold)" stroke-width="1" stroke-dasharray="4 3" fill="none">
      <line x1="108" y1="300" x2="408" y2="300"/>
      <line x1="103" y1="517" x2="1150" y2="517"/>
      <line x1="103" y1="945" x2="1150" y2="945"/>
      <line x1="103" y1="517" x2="103" y2="945"/>
      <line x1="413" y1="517" x2="413" y2="945"/>
      <line x1="630" y1="517" x2="630" y2="945"/>
      <line x1="940" y1="517" x2="940" y2="945"/>
      <line x1="665" y1="300" x2="905" y2="300"/>
      <path d="M305 1050 L355 1050"/>
      <path d="M835 1050 L880 1050"/>
    </g>
    <g stroke="var(--fold)" stroke-width="1" fill="none">
      <path d="M630 300 H665 V312"/><path d="M940 300 H905 V312"/>
    </g>
  </svg>

  <div class="layer manual">
    <p><span class="lang">UK</span> <strong>InkJet printer cartridge</strong></p>
    <p>Take out cartridge from the wrapping just before use. Do not shake and press the unpacked cartridge, the cartridge contains ink which can grime your hands and clothes. Please refer to the printer instruction manual before installing the cartridge. Keep out of the reach of children. Protect from direct solar radiation. Store by temperature range displayed on the wrapping.</p>
    <div class="gap"></div>
    <p><span class="lang">SLO</span> <strong>Atramentová tlačová kazeta</strong></p>
    <p class="just">Nevybaľujte kazetu z ochranného obalu, pokiaľ ju nebudete okamžite inštalovať do tlačiarne. Pred inštaláciou do tlačiarne odstráňte ochranný obal a ochrannú pásku. Netraste a nestláčajte rozbalenú kazetu, obsahuje atrament, ktorý môže vystreknúť na Vaše ruky, odev alebo inde. Pri inštalácii kazety do tlačiarne postupujte podľa užívateľského návodu k tlačiarni. Skladujte mimo dosahu detí. Chráňte pred priamym slnečným žiarením. Skladujte v teplotnom rozmedzí zobrazenom na obale.</p>
    <hr>
    <p>Use before <strong>24 months</strong> from production date.</p>
    <p>Spotrebujte do <strong>24 mesiacov</strong> od dátumu výroby.</p>
    <hr>
    <p>All brand names and trademarks are the properties of their respective holders and are referred to here for descriptive purposes only.</p>
    <div style="height:6px"></div>
    <p>Všetky názvy a obchodné mená sú majetkom ich vlastníkov, v žiadnom prípade nie sú dotknuté práva ich majiteľov a sú znázornené len pre znázornenie kompatibility.</p>
  </div>

  <div class="layer brand"><span>sylvanto</span><span class="dot"></span></div>

  <div class="layer title title-front"><div><span class="eco">ECO</span>INK</div><div class="line2">CARTIDGE</div></div>
  <div class="layer title title-side"><div><span class="eco">ECO</span>INK</div><div class="line2">CARTIDGE</div></div>

  <div class="layer compat-label">Compatible with</div>
  <div class="layer compat-box"></div>
  <div class="layer prod-label">Production Date/Dátum výroby</div>
  <div class="layer prod-box"></div>

  <div class="layer specs">
    <p>Made in Europe</p>
    <p>Part No.:</p>
    <p>ISO 9001 / ISO 14001</p>
  </div>
</div>
</body>
</html>
```